Velmora Investments - stationery for luxury, exclusive property investment company

We need stationery (letterhead, folder, compliments slip and envelope) and business cards which will reflect our luxury brand.

I have attached some design examples that we like.

We are an investment company which buys property to provide accommodation for corporate customers.

The design of the stationery needs to be be simple, refined, understated, luxury and very tasteful.

The design should communicate luxury and exclusivity, without being ostentatious.

Logo files are attached
Updates

Please can designers re-read the brief, and make sure the logo is in gold on either on a navy or white background.

Target Market(s)

Wealthy customers

Contact Information for Business Card

Laura Penhaligon-Ward
Director
Velmora Investments Limited
email: laura@velmorainvestments-example.co.uk
mob: 07700900412

Font styles to use
Serif

Colors

Designer to choose colors to be used in the design.

Requirements
Must have
• The logo must be gold on either a white or navy background as per the attached logos.
• The stationery MUST have the following information:
• Velmora Investments Limited
• The Larches
• Wexley Rise
• Ashmere
• ZX19 2QP
• Company Number: 48273615 (Registered in England and Wales)
• The letterhead must also have the two attached logos for the KPV and the KPV accreditation scheme. They do not need to be large.
Nice to have
• A watermark, navy banding either top or bottom.
Should not have
• Anything that looks budget.

```html
<!DOCTYPE html>
<html lang="en">
<head>
<meta charset="utf-8">
<title>Velmora Investments – Stationery</title>
<link href="https://fonts.googleapis.com/css2?family=Cinzel:wght@400;500&family=Montserrat:wght@500;600&display=swap" rel="stylesheet">
<style>
  :root{
    --navy:#150633;
    --gold:#c9a23e;
    --gold-soft:#d9b860;
    --silver:#8c9298;
    --watermark:#e6e6e6;
    --ink:#1b1446;
    --badge-red:#e0141f;
    --badge-orange:#f04a23;
    --paper:#ffffff;
    --edge:#ececec;
  }
  *{box-sizing:border-box;margin:0;padding:0}
  html,body{width:1200px;height:1198px;overflow:hidden;background:#fff}
  .board{position:relative;width:1200px;height:1198px;border:1px solid #9a9a9a;background:#fff}
  .sheet{position:absolute;width:364px;height:477px;background:var(--paper);
    border:1px solid var(--edge);box-shadow:0 2px 10px rgba(0,0,0,.06);overflow:hidden}
  .folder{left:33px;top:44px;background:var(--navy);border:none}
  .lh-ribbon{left:418px;top:45px}
  .lh-framed{left:803px;top:44px}
  .lh-band{left:166px;top:607px}
  .lh-centred{left:593px;top:610px}

  .brand{font-family:"Cinzel",serif;font-weight:400;color:var(--gold);text-align:center;line-height:1}
  .brand .name{display:block;letter-spacing:.04em}
  .brand .sub{display:flex;align-items:center;gap:4px;justify-content:center;letter-spacing:.35em}
  .brand .sub::before,.brand .sub::after{content:"";height:1px;width:14px;background:currentColor}
  .mark{display:block;border-radius:50%;border:2px solid currentColor;margin:0 auto}

  .watermark{position:absolute;left:50%;width:82px;height:82px;margin-left:-41px;
    border-radius:50%;border:7px solid var(--watermark)}

  .folder-mark{position:absolute;left:0;right:0;top:160px;color:var(--silver)}
  .folder-mark .mark{width:132px;height:132px;border-width:6px;margin-bottom:16px}
  .folder-mark .name{font-size:21px}
  .folder-mark .sub{font-size:9px;margin-top:6px}

  .ribbon{position:absolute;left:133px;top:0;width:114px;height:106px;background:var(--navy);
    clip-path:polygon(0 0,100% 0,100% 100%,50% 75%,0 100%);padding-top:12px}
  .ribbon .mark{width:28px;height:28px;margin-bottom:10px}
  .ribbon .name{font-size:11.5px}
  .ribbon .sub{font-size:6px;margin-top:3px}

  .footer{position:absolute;left:12px;bottom:17px;width:340px;color:var(--ink);font-family:"Montserrat",sans-serif}
  .footer .company{font-family:"Cinzel",serif;font-size:9.5px;font-weight:500;letter-spacing:.03em;
    width:262px;border-bottom:1px solid var(--ink);padding:0 0 1px 2px}
  .footer .address{font-size:7.4px;font-weight:600;margin-top:6px}
  .footer .reg{font-size:5.2px;font-weight:600;margin-top:4px}
  .badges{position:absolute;right:0;top:-1px;display:flex;gap:5px}
  .badge{width:32px;height:17px;background:var(--badge-red);border-radius:1px}
  .badge.alt{width:34px;height:14px;background:var(--badge-orange);margin-top:3px}

  .top-lockup{position:absolute;left:18px;top:20px;display:flex;align-items:center;gap:10px;color:var(--gold)}
  .top-lockup .mark{width:40px;height:40px;border-width:3px;margin:0}
  .top-lockup .brand{text-align:left}
  .top-lockup .name{font-size:15.5px}
  .top-lockup .sub{font-size:7.5px;margin-top:3px}

  .framed-footer{position:absolute;left:14px;right:14px;top:411px;height:52px;text-align:center;color:var(--gold)}
  .corner{position:absolute;top:0;width:32px;height:52px;border-bottom:2px solid var(--gold)}
  .corner.left{left:0;border-left:2px solid var(--gold)}
  .corner.right{right:0;border-right:2px solid var(--gold)}
  .framed-footer .company{font-family:"Cinzel",serif;font-size:8.6px;letter-spacing:.03em;margin-top:-4px}
  .framed-footer .address{font-family:"Montserrat",sans-serif;font-size:7.6px;font-weight:500;margin-top:3px}
  .framed-footer .reg{font-family:"Montserrat",sans-serif;font-size:5px;font-weight:600;margin-top:2px}
  .framed-footer .badges{position:static;justify-content:center;margin-top:7px}

  .band{position:absolute;left:0;top:0;width:100%;height:80px;background:var(--navy);
    display:flex;align-items:center;justify-content:center;gap:10px;color:var(--gold)}
  .band .mark{width:40px;height:40px;border-width:3px;margin:0}
  .band .brand{text-align:left}
  .band .name{font-size:15.5px}
  .band .sub{font-size:7.5px;margin-top:3px}

  .centred-lockup{position:absolute;left:0;right:0;top:20px;color:var(--gold)}
  .centred-lockup .mark{width:76px;height:76px;border-width:4px;margin-bottom:18px}
  .centred-lockup .name{font-size:24px;color:var(--gold-soft)}
  .centred-lockup .sub{font-size:12.5px;margin-top:5px;color:var(--gold-soft)}
  .centred-lockup .sub::before,.centred-lockup .sub::after{width:26px}
</style>
</head>
<body>
<main class="board">

  <section class="sheet folder" aria-label="Presentation folder cover">
    <div class="brand folder-mark">
      <span class="mark"></span>
      <span class="name">Velmora</span>
      <span class="sub">Investments</span>
    </div>
  </section>

  <section class="sheet lh-ribbon" aria-label="Letterhead with navy ribbon">
    <div class="ribbon brand">
      <span class="mark"></span>
      <span class="name">Velmora</span>
      <span class="sub">Investments</span>
    </div>
    <span class="watermark" style="top:205px"></span>
    <footer class="footer">
      <p class="company">VELMORA INVESTMENTS LIMITED</p>
      <p class="address">THE LARCHES, WEXLEY RISE, ASHMERE, ZX19 2QP ,</p>
      <p class="reg">COMPANY NUMBER: 48273615 (REGISTERED IN ENGLAND AND WALES)</p>
      <div class="badges"><span class="badge"></span><span class="badge alt"></span></div>
    </footer>
  </section>

  <section class="sheet lh-framed" aria-label="Letterhead with gold frame">
    <div class="top-lockup">
      <span class="mark"></span>
      <div class="brand"><span class="name">Velmora</span><span class="sub">Investments</span></div>
    </div>
    <span class="watermark" style="top:205px"></span>
    <div class="framed-footer">
      <span class="corner left"></span><span class="corner right"></span>
      <p class="company">VELMORA INVESTMENTS LIMITED</p>
      <p class="address">THE LARCHES, WEXLEY RISE, ASHMERE, ZX19 2QP</p>
      <p class="reg">COMPANY NUMBER: 48273615 (REGISTERED IN ENGLAND AND WALES)</p>
      <div class="badges"><span class="badge"></span><span class="badge alt"></span></div>
    </div>
  </section>

  <section class="sheet lh-band" aria-label="Letterhead with navy top band">
    <header class="band">
      <span class="mark"></span>
      <div class="brand"><span class="name">Velmora</span><span class="sub">Investments</span></div>
    </header>
    <span class="watermark" style="top:205px"></span>
    <footer class="footer">
      <p class="company">VELMORA INVESTMENTS LIMITED</p>
      <p class="address">THE LARCHES, WEXLEY RISE, ASHMERE, ZX19 2QP ,</p>
      <p class="reg">COMPANY NUMBER: 48273615 (REGISTERED IN ENGLAND AND WALES)</p>
      <div class="badges"><span class="badge"></span><span class="badge alt"></span></div>
    </footer>
  </section>

  <section class="sheet lh-centred" aria-label="Letterhead with centred gold lockup">
    <div class="brand centred-lockup">
      <span class="mark"></span>
      <span class="name">Velmora</span>
      <span class="sub">Investments</span>
    </div>
    <span class="watermark" style="top:205px"></span>
    <footer class="footer">
      <p class="company">VELMORA INVESTMENTS LIMITED</p>
      <p class="address">THE LARCHES, WEXLEY RISE, ASHMERE, ZX19 2QP ,</p>
      <p class="reg">COMPANY NUMBER: 48273615 (REGISTERED IN ENGLAND AND WALES)</p>
      <div class="badges"><span class="badge"></span><span class="badge alt"></span></div>
    </footer>
  </section>

</main>
</body>
</html>
```